Professional Home Buyer business card needed

I need a pretty straight forward business card designed. We help people that NEED to sell their homes solve problems. We perform all types of Real Estate transactions including flip, wholesale, investment, rental property and multi family. The card will mainly be used to give to prospective Sellers but will also be given to Real Estate Investors as well. It should professional and very easy to read, most clients are older people.

Target Market(s)

Distressed home sellers as well as Real Estate investors

Industry/Entity Type

Real Estate

Contact Information for Business Card

should be a professional layout

Colors
ec1f27
ffffff
000000

Requirements
Must have
• Large logo on back and smaller one on front. should utilize Red, white, and black.
• I am thinking of using a soft touch coating on the card so keep that in mind.
• Contact info should be very easy to read, think older clients.
Nice to have
• I would like to see a design with rounded corners on the card
Should not have
• pictures of homes or other home graphics.

```html
<!DOCTYPE html>
<html lang="en">
<head>
<meta charset="utf-8">
<title>Harbor Home Buyers – Business Card</title>
<link href="https://fonts.googleapis.com/css2?family=Oswald:wght@500;700&family=Open+Sans:wght@400;600&display=swap" rel="stylesheet">
<style>
  :root {
    --red: #ec1f27;
    --white: #ffffff;
    --black: #000000;
    --card-dark: #141414;
    --stage: #2b2b2b;
    --ink-soft: #2a2a2a;
  }
  * { box-sizing: border-box; margin: 0; padding: 0; }
  html, body { width: 1200px; height: 716px; overflow: hidden; }
  body {
    background: var(--stage);
    font-family: "Open Sans", Arial, sans-serif;
    position: relative;
  }
  .card {
    position: absolute;
    width: 520px;
    height: 297px;
    border-radius: 22px;
    overflow: hidden;
  }
  /* Back side */
  .card-back {
    left: 50px; top: 210px;
    background: var(--card-dark);
    display: flex; flex-direction: column;
    align-items: center; justify-content: center;
  }
  .tagline {
    font-family: "Oswald", Arial, sans-serif;
    font-weight: 500;
    font-size: 14px;
    letter-spacing: 5px;
    text-transform: uppercase;
    color: var(--white);
    margin-bottom: 12px;
    white-space: nowrap;
  }
  .brand {
    display: flex; align-items: center; gap: 12px;
  }
  .brand-mark { width: 16px; height: 16px; background: var(--red); flex: none; }
  .brand-name {
    font-family: "Oswald", Arial, sans-serif;
    font-weight: 700;
    text-transform: uppercase;
    white-space: nowrap;
  }
  .card-back .brand-name { font-size: 40px; letter-spacing: 3px; color: var(--white); }
  .card-back .website {
    margin-top: 28px;
    font-size: 12px;
    letter-spacing: 1.5px;
    color: var(--red);
  }
  /* Front side */
  .card-front {
    left: 630px; top: 210px;
    background: var(--white);
    padding: 34px 30px 30px 34px;
  }
  .person-name {
    font-family: "Oswald", Arial, sans-serif;
    font-weight: 700;
    font-size: 30px;
    line-height: 1;
    color: var(--black);
    text-transform: uppercase;
    letter-spacing: 0.5px;
  }
  .person-title {
    font-family: "Oswald", Arial, sans-serif;
    font-weight: 500;
    font-size: 14px;
    color: var(--red);
    text-transform: uppercase;
    letter-spacing: 1px;
    margin-top: 4px;
  }
  .title-rule { width: 60px; height: 3px; background: var(--red); margin-top: 8px; }
  .contact-list {
    position: absolute; left: 34px; bottom: 32px;
    list-style: none;
  }
  .contact-list li {
    display: flex; align-items: center; gap: 10px;
    font-size: 14px; line-height: 24px; color: var(--ink-soft);
    white-space: nowrap;
  }
  .contact-list svg { width: 13px; height: 13px; fill: var(--red); flex: none; }
  .front-logo {
    position: absolute; right: 30px; top: 112px;
    text-align: center;
  }
  .front-logo .tagline { font-size: 9px; letter-spacing: 3px; color: var(--black); margin-bottom: 6px; }
  .front-logo .brand { gap: 8px; }
  .front-logo .brand-mark { width: 10px; height: 10px; }
  .front-logo .brand-name { font-size: 20px; letter-spacing: 1.5px; color: var(--black); }
</style>
</head>
<body>
  <section class="card card-back" aria-label="Card back">
    <p class="tagline">We make selling simple!</p>
    <div class="brand">
      <span class="brand-mark"></span>
      <span class="brand-name">Harbor Home Buyers</span>
    </div>
    <p class="website">www.harborhomesales.com</p>
  </section>

  <section class="card card-front" aria-label="Card front">
    <h1 class="person-name">Dana Whitlock</h1>
    <p class="person-title">President</p>
    <div class="title-rule"></div>

    <div class="front-logo">
      <p class="tagline">We make selling simple!</p>
      <div class="brand">
        <span class="brand-mark"></span>
        <span class="brand-name">Harbor Home Buyers</span>
      </div>
    </div>

    <ul class="contact-list">
      <li>
        <svg viewBox="0 0 24 24" aria-hidden="true"><path d="M6.6 10.8a15.1 15.1 0 0 0 6.6 6.6l2.2-2.2c.3-.3.7-.4 1-.2 1.1.4 2.3.6 3.6.6.6 0 1 .4 1 1V20c0 .6-.4 1-1 1A17 17 0 0 1 3 4c0-.6.4-1 1-1h3.5c.6 0 1 .4 1 1 0 1.3.2 2.5.6 3.6.1.3 0 .7-.2 1z"/></svg>
        316-555-0142
      </li>
      <li>
        <svg viewBox="0 0 24 24" aria-hidden="true"><path d="M2 5h20v14H2zm2 2v.5l8 5 8-5V7l-8 5z"/></svg>
        dana@harborhomesales.com
      </li>
      <li>
        <svg viewBox="0 0 24 24" aria-hidden="true"><path d="M12 2a10 10 0 1 0 0 20 10 10 0 0 0 0-20zm6.9 9h-3a15 15 0 0 0-1.3-6A8 8 0 0 1 18.9 11zM12 4c.9 1.2 1.7 3.6 1.9 7h-3.8c.2-3.4 1-5.8 1.9-7zM9.4 5a15 15 0 0 0-1.3 6h-3A8 8 0 0 1 9.4 5zM5.1 13h3a15 15 0 0 0 1.3 6A8 8 0 0 1 5.1 13zM12 20c-.9-1.2-1.700-3.6-1.9-7h3.8c-.2 3.4-1 5.8-1.9 7zm2.6-1a15 15 0 0 0 1.3-6h3a8 8 0 0 1-4.3 6z"/></svg>
        www.harborhomesales.com
      </li>
      <li>
        <svg viewBox="0 0 24 24" aria-hidden="true"><path d="M12 2a7 7 0 0 0-7 7c0 5 7 13 7 13s7-8 7-13a7 7 0 0 0-7-7zm0 9.5a2.5 2.5 0 1 1 0-5 2.5 2.5 0 0 1 0 5z"/></svg>
        P.O. Box 112, Fairview, KS 67010
      </li>
    </ul>
  </section>
</body>
</html>
```